Football tournament flyer

I would like a quick turn around for this please.
I need a flyer to promote an 11 aside football tournament I am organising to celebrate the 23rd independence of my country Somaliland. Please use the national colours of our flag in the flyer, I have attached a file for your consideration.
The tournament will take place on 10/05/2014, from 9am - 8pm. The venue will be Corvell Open Space, Tresham Lane, Enfield, EN7 2QJ.
Refreshments, food and entertainment will be provided.
The name of the cup is Warsadeq Cup.
Spaces are limited and the entry fee per team is £200. All proceeds are for charity projects in Somaliland.
To register a team contact Bashir Yusuf on 07591 248 613 or Warsame Hirsi on 07462 571 380.
The best players will have the opportunity to represent Somaliland in an international game on the 17/05/2014.
The tournament is organised by Dalmar FC and Kindwell Foundation.
Industry/Entity Type
Entertainment

```html
<!DOCTYPE html>
<html lang="en">
<head>
<meta charset="utf-8">
<title>Warsadeq Cup – 11 Aside Football Tournament</title>
<link rel="stylesheet" href="https://fonts.googleapis.com/css2?family=Anton&family=Archivo+Black&family=Arimo:wght@400;700&family=Kaushan+Script&family=Tinos:wght@400;700&display=swap">
<style>
  :root{
    --frame:#2a1c17;
    --white:#ffffff;
    --black:#111111;
    --red:#e42d24;
    --red-deep:#c81f19;
    --lime:#8dc63f;
    --green-light:#a8d35a;
    --green:#5fae34;
    --crowd:#1b1b1b;
  }
  *{margin:0;padding:0;box-sizing:border-box}
  html,body{width:935px;height:1200px;overflow:hidden;background:var(--frame)}
  .flyer{position:relative;width:935px;height:1200px;background:var(--frame)}
  .panel{position:absolute;left:27px;top:27px;width:881px;height:1141px;border:3px solid var(--white);overflow:hidden;background:var(--red)}
  .hero-art{position:absolute;left:0;top:0;width:100%;height:850px;
    background:linear-gradient(180deg,var(--green-light) 0%,var(--green) 40%,#6fb83c 62%,#2e3a22 74%,var(--crowd) 84%);}
  .wave{position:absolute;left:0;top:800px;width:100%;height:100px}
  .abs{position:absolute;line-height:1;white-space:nowrap}
  .celebrate{left:30px;top:60px;font-family:"Kaushan Script",cursive;font-size:40px;color:var(--black);
    transform:rotate(-15deg);transform-origin:left top;line-height:1.15;text-shadow:0 0 4px var(--white),0 0 2px var(--white)}
  .organised{left:417px;top:325px;font-family:"Arimo",sans-serif;font-weight:700;font-size:27px;color:var(--black);text-shadow:0 0 3px var(--white)}
  .organisers{left:413px;top:362px;font-family:"Arimo",sans-serif;font-weight:700;font-size:16px;color:var(--black)}
  .cup-name{left:0;width:100%;text-align:center;top:378px;font-family:"Anton",sans-serif;font-size:84px;letter-spacing:3px;color:var(--red);
    -webkit-text-stroke:3px var(--white);paint-order:stroke fill;text-shadow:3px 4px 0 rgba(0,0,0,.45)}
  .format{left:0;width:100%;text-align:center;top:470px;font-family:"Tinos",serif;font-size:156px;color:var(--black);text-shadow:0 0 6px rgba(255,255,255,.7)}
  .event-type{left:0;width:100%;text-align:center;top:610px;font-family:"Tinos",serif;font-size:45px;color:var(--black);text-shadow:0 0 4px rgba(255,255,255,.8)}
  .date,.hours{left:0;width:100%;text-align:center;font-family:"Tinos",serif;font-weight:700;font-size:60px;color:var(--white);
    -webkit-text-stroke:2px var(--black);paint-order:stroke fill}
  .date{top:658px}
  .hours{top:710px}
  .venue,.extras{left:0;width:100%;text-align:center;font-family:"Tinos",serif;font-weight:700;font-size:20px;color:var(--white)}
  .venue{top:770px}
  .extras{top:797px}
  .fee{left:0;width:100%;text-align:center;top:888px;font-family:"Archivo Black",sans-serif;font-size:21px;color:var(--black);line-height:1.6}
  .fee .hi{color:var(--white)}
  .register{position:absolute;left:31px;top:972px;width:389px;height:146px;background:var(--lime);padding:8px}
  .register-head{background:var(--white);font-family:"Arimo",sans-serif;font-size:21px;color:var(--black);padding:5px 14px;width:340px;line-height:1.2}
  .register-body{font-family:"Arimo",sans-serif;font-size:19px;color:var(--black);padding:14px 6px 0;line-height:1.55}
  .note{left:447px;top:980px;font-family:"Arimo",sans-serif;font-size:22px;color:var(--white);line-height:1.42}
</style>
</head>
<body>
<div class="flyer">
  <div class="panel">
    <div class="hero-art" role="img" aria-label="Grunge green football artwork with a waving Somaliland flag, a football, a player in motion and a cheering crowd silhouette"></div>
    <svg class="wave" viewBox="0 0 881 100" preserveAspectRatio="none" aria-hidden="true">
      <path d="M0 76 C250 58 600 34 881 22 L881 100 L0 100 Z" fill="var(--white)"/>
      <path d="M0 92 C260 76 600 54 881 44 L881 100 L0 100 Z" fill="var(--red)"/>
    </svg>

    <p class="abs celebrate">Celebrating 23rd<br>&nbsp;&nbsp;Independence day</p>
    <p class="abs organised">Organised by</p>
    <p class="abs organisers">Dalmar FC and Kindwell Foundation</p>
    <h1 class="abs cup-name">WARSADEQ CUP</h1>
    <p class="abs format">11 ASIDE</p>
    <p class="abs event-type">FOOTBALL TOURNAMENT</p>
    <p class="abs date">10/05/2014,</p>
    <p class="abs hours">from 9am - 8pm</p>
    <p class="abs venue">Corvell Open Space, Tresham Lane, Enfield, EN7 2QJ.</p>
    <p class="abs extras">Refreshments, food and entertainment will be provided.</p>

    <p class="abs fee">Spaces are limited and the <span class="hi">entry fee per team is £200.</span><br>All proceeds are for charity projects in Somaliland.</p>

    <div class="register">
      <p class="register-head">To register a team contact</p>
      <p class="register-body">Bashir Yusuf on 07591 248 613<br>or Warsame Hirsi on 07462 571 380.</p>
    </div>

    <p class="abs note">*The best players will have the<br>opportunity to represent Somaliland<br>in an international game on the<br>17/05/2014.</p>
  </div>
</div>
</body>
</html>
```